Qarnetix EIRL Business Card Design Project

We need a business card design for a New Business Intelligence Consultant. We bring a complete service to the client from first consulting meeting to help desk and system improvement.

I will upload the company logo and I like to use the logo colors on the card. Feel free to use all logo components on the design, for example one side with the black logo using complete card and the other side only the red shape (is an example, feel absolutely free :)).

The principal idea is to sell a professional service and a modern company.

Target Market(s)

IT Business Intelligence Clients

Industry/Entity Type

Professional Service

Requirements
Nice to have
• - Use the logo colors and minimize white sections.
- Rounded borders
Should not have
• I don't want to see any references to people working on a meeting or office photos or any computers related logos.

```html
<!DOCTYPE html>
<html lang="es">
<head>
<meta charset="utf-8">
<title>Qarnetix EIRL — Tarjeta de presentación</title>
<link href="https://fonts.googleapis.com/css2?family=Ubuntu:wght@300;400&display=swap" rel="stylesheet">
<style>
  :root {
    --page: #ffffff;
    --card: #080909;
    --red: #e3120f;
    --white: #f2f2f2;
    --grey: #8c8c8c;
  }
  html, body {
    margin: 0;
    padding: 0;
    width: 1200px;
    height: 400px;
    overflow: hidden;
    background: var(--page);
    font-family: "Ubuntu", Arial, sans-serif;
  }
  .canvas {
    position: relative;
    width: 1200px;
    height: 400px;
  }
  .card {
    position: absolute;
    top: 27px;
    width: 565px;
    height: 345px;
    background: var(--card);
    border-radius: 46px;
  }
  .card--front { left: 25px; }
  .card--back { left: 610px; }

  .brand {
    position: absolute;
    display: flex;
    align-items: center;
    gap: 12px;
  }
  .brand__square {
    width: 30px;
    height: 30px;
    background: var(--grey);
  }
  .brand__name {
    color: var(--red);
    font-weight: 400;
    line-height: 1;
  }
  .card--front .brand {
    left: 173px;
    top: 154px;
  }
  .card--front .brand__name { font-size: 40px; }

  .card--back .brand {
    left: 172px;
    top: 166px;
  }
  .card--back .brand__name { font-size: 17px; }

  .contact {
    position: absolute;
    left: 282px;
    top: 70px;
    margin: 0;
    padding: 0;
    list-style: none;
    font-size: 9px;
    font-weight: 300;
    color: var(--white);
    line-height: 11px;
  }
  .contact__label {
    display: inline-block;
    width: 19px;
    color: var(--red);
  }

  .person {
    position: absolute;
    left: 282px;
    top: 161px;
  }
  .person__name {
    margin: 0;
    font-size: 12.5px;
    font-weight: 400;
    color: var(--white);
    letter-spacing: 0.2px;
  }
  .person__role {
    margin: 1px 0 0;
    font-size: 10px;
    font-weight: 300;
    color: var(--red);
  }

  .address {
    position: absolute;
    left: 282px;
    top: 236px;
    font-style: normal;
    font-size: 9px;
    font-weight: 300;
    color: var(--white);
    line-height: 11px;
    letter-spacing: 0.2px;
  }
</style>
</head>
<body>
<main class="canvas">
  <section class="card card--front" aria-label="Anverso">
    <div class="brand">
      <span class="brand__square"></span>
      <span class="brand__name">qarnetix</span>
    </div>
  </section>

  <section class="card card--back" aria-label="Reverso">
    <ul class="contact">
      <li><span class="contact__label">p</span>+56 (9) 90012345</li>
      <li><span class="contact__label">e</span>tomas@qarnetix.cl</li>
      <li><span class="contact__label">w</span>www.qarnetix.cl</li>
    </ul>

    <div class="brand">
      <span class="brand__name">qarnetix</span>
    </div>

    <div class="person">
      <p class="person__name">Tomás Ibarra L.</p>
      <p class="person__role">Gerente General</p>
    </div>

    <address class="address">
      Av. Los Aromos Sur 250<br>
      Of:310. Las Condes, Santiago
    </address>
  </section>
</main>
</body>
</html>
```